Website for Sports and Exercise Medicine Doctor with active research in stem cells therapies.

I am a sports and exercise medicine doctor with research interests in the cutting edge areas of biological therapies, most notable stem cells. None of my patients are dying of anything, and most of them come to see me to decrease their pain, so they can get back to what they want to do.

The approach i then take is to decrease their pain and support them to achieve the things they wish to achieve. Most people start at "Just make it stop hurting doc" , but I try to move them towards something more important over time.

I would like the website to be very different to other "Doctor or medical websites" in its look. No pictures of doctors in white coats and no pictures of fit old people smiling. I would potentially like the fist thing seen to be a quote:

"Less pain. Everybody wants it, but what are you going to do, once you've got it?"

(But this is only an idea, I am open to anything)

The website will need a couple of things

1. "Locations" I work
2. "Research" I am involved in
3. "Sort Me out" - Clinical information for people to access
4. "Social" - imbedded chirpline and friendgrid
5. "Blog" - imbedded postmill blog
6. "Bio" - the usual bio-stuff

The "Sort Me out" - pages I would like to have the functionality as seen in this site http://www.vandrolix.com.au/platelet/. I intend to put disease topics into these pages (eg Achilles tehdinopathy, osteoarthritis etc etc etc). Once again I am not wedded to this but something along these lines would be good.

To give you an idea these are some sites I like
http://www.harborlantern.com/
http://quimbet.com/
http://orvanstudio.com.sg/
http://milbonhonestkettle.com/
http://www.tessmonthly.com/
http://gravwick.com/#offering
http://pelicanworks.tv/
http://tidalnova.com/
http://foxledger.co.uk/#about

Target Market(s)

20-80 year old.
People with tendon injuries
People with osteoarthritis
People interested in stem cells
I will build the site over time to contain information on multiple sporting injuries and musculoskeletal disorders. It will also become a site for the latest on stem cell research particularly in the area of osteoarthritis.

Industry/Entity Type

Medical

Font styles to use
Sans Serif

Colors
ffffff

Requirements
Nice to have
• To give you an idea these are some sites I like
http://quimbet.com/
http://pelicanworks.tv/
http://tidalnova.com/
Should not have
• Pictures of doctors in white coats or old fit people smiling

```html
<!DOCTYPE html>
<html lang="en">
<head>
<meta charset="utf-8">
<title>Sports &amp; Exercise Medicine</title>
<link rel="stylesheet" href="https://fonts.googleapis.com/css2?family=Open+Sans:wght@300;400;600;700&display=swap">
<style>
:root{
  --yellow:#f2be00;
  --ink:#222222;
  --text:#6f6f6f;
  --muted:#9a9a9a;
  --line:#dddddd;
  --footer:#262324;
  --footer-panel:#161415;
  --footer-text:#9e9e9e;
  --white:#ffffff;
}
*{margin:0;padding:0;box-sizing:border-box}
html,body{width:780px;height:1200px;overflow:hidden;background:var(--white)}
body{position:relative;font-family:"Open Sans",Arial,sans-serif;color:var(--text)}
.abs{position:absolute}

/* header & hero */
.hero-photo{left:0;top:0;width:780px;height:377px;
  background:radial-gradient(ellipse 230px 260px at 500px 210px,#e9c46a 0%,rgba(233,196,106,.35) 45%,rgba(233,196,106,0) 75%),
  linear-gradient(90deg,#eeeeec 0%,#dcdcda 40%,#c9c6c0 70%,#9ea0a2 100%);}
.hero-rule{left:0;top:377px;width:780px;height:2px;background:var(--yellow)}
.nav-strip{left:290px;top:0;width:490px;height:11px;background:#4f5753}
.nav-bar{left:286px;top:11px;width:494px;height:25px;background:var(--yellow)}
.logo-plate{left:0;top:0;width:330px;height:40px}
.logo{left:197px;top:8px;font-size:19px;font-weight:600;color:var(--yellow);letter-spacing:-.5px}
.social{left:589px;top:2px;display:flex;gap:2px}
.social span{width:7px;height:7px;border-radius:50%;background:var(--white)}
.nav{left:413px;top:20px;display:flex;gap:23px;font-size:6.5px;font-weight:700;color:var(--ink)}
.nav-marker{left:418px;top:12px;width:0;height:0;border-left:3px solid transparent;border-right:3px solid transparent;border-top:4px solid var(--white)}
.quote{left:155px;top:120px;font-size:14px;letter-spacing:-.6px;color:var(--ink)}
.quote .l1{font-weight:600}
.quote .l2{display:inline-block;margin:3px 0 0 12px;padding:1px 3px;background:#4a4a48;color:var(--yellow);font-weight:600;text-transform:uppercase}
.quote .l3{margin:4px 0 0 102px;text-transform:uppercase}

/* section heads */
.divider{height:1px;background:var(--line)}
.divider i{position:absolute;top:-1px;height:3px;background:var(--yellow)}
.sec-title{font-size:15px;font-weight:400;letter-spacing:-.7px;color:var(--ink);text-align:center;text-transform:uppercase}
.sec-title b{color:var(--yellow);font-weight:600}
.sec-desc{font-size:5px;line-height:6.5px;color:var(--muted);text-align:center}

/* service cards */
.card{top:460px;width:127px;height:161px;border:1px solid #d9d9d9;border-radius:4px;box-shadow:0 1px 2px rgba(0,0,0,.12);overflow:hidden}
.card .thumb{height:52px;background:linear-gradient(180deg,#a9c8e2 0%,#e3e6e6 45%,#9a8576 75%,#8a3b2c 100%)}
.card h4{margin:13px 6px 5px;font-size:6.5px;font-weight:400;color:#444}
.card p{margin:0 6px;font-size:5.4px;line-height:8.4px;color:var(--text);letter-spacing:-.1px}
.card a{display:block;margin:10px 6px 0;font-size:6px;color:var(--yellow);text-decoration:none}

/* accordion */
.acc-head{left:156px;top:744px;width:222px;height:12px;background:var(--yellow);color:var(--white);font-size:5.5px;line-height:12px;padding-left:13px}
.acc-body{left:157px;top:762px;width:221px;font-size:5.3px;line-height:7.3px;color:#555}
.acc-row{left:157px;width:221px;height:15px;border-bottom:1px solid var(--line);font-size:5.5px;line-height:13px;color:#555;font-weight:600}
.acc-row span{position:absolute;right:4px;top:0;color:var(--yellow);font-size:10px;font-weight:300;line-height:13px}

/* blog */
.post{left:419px;width:182px}
.date{position:absolute;left:0;top:0;width:12px}
.date .d1{height:11px;background:#444;color:var(--white);font-size:3.5px;text-align:center;line-height:5px}
.date .d2{height:10px;background:var(--yellow);color:var(--white);font-size:5px;text-align:center;line-height:10px;font-weight:700}
.post h5{margin-left:19px;font-size:5.5px;font-weight:600;color:#444}
.post .meta{margin:3px 0 0 19px;font-size:5px;color:var(--muted);display:flex;align-items:center;gap:3px}
.post p{margin:3px 0 0 19px;font-size:5.1px;line-height:7.3px;color:var(--muted);letter-spacing:-.1px}
.post p em{font-style:normal;color:var(--yellow)}

/* testimonial */
.testimonial{left:180px;top:975px;width:420px;text-align:center;font-size:6.8px;line-height:9px;color:#555}
.author{left:0;top:1003px;width:780px;text-align:center;font-size:6px;color:#666}
.author b{color:var(--yellow);font-style:italic}

/* footer */
.footer{left:0;top:1058px;width:780px;height:121px;background:var(--footer);border-top:2px solid #3d4744}
.f-title{top:1072px;font-size:12px;font-weight:300;color:var(--white);letter-spacing:-.5px}
.f-title b{font-weight:600}
.f-links{left:156px;top:1094px;list-style:none;font-size:6.2px;line-height:12.1px;color:#bdbdbd}
.f-links li::before{content:"\2192";color:var(--yellow);margin-right:6px}
.f-text{top:1094px;font-size:6.3px;line-height:10px;color:var(--footer-text)}
.f-more{font-size:7px;color:var(--white);font-weight:600}
.f-more span{color:var(--yellow)}
.contact{left:515px;width:108px;height:20px;background:var(--footer-panel);display:flex;align-items:center;gap:7px;padding-left:7px;font-size:5px;line-height:6px;color:var(--white)}
.bottom{left:156px;top:1184px;width:467px;display:flex;justify-content:space-between;font-size:6px;color:#555}
</style>
</head>
<body>

<!-- header and hero -->
<div class="abs hero-photo" role="img" aria-label="Photograph of a smiling woman in a yellow sports top training on a gym machine, blurred gym behind"></div>
<div class="abs hero-rule"></div>
<div class="abs nav-strip"></div>
<div class="abs nav-bar"></div>
<svg class="abs logo-plate" width="330" height="40" viewBox="0 0 330 40"><polygon points="0,0 310,0 282,38 0,40" fill="#ffffff"/><polygon points="282,38 310,0 313,0 285,38" fill="#cfcfcf"/></svg>
<div class="abs logo">LOGO</div>
<div class="abs social"><span></span><span></span><span></span><span></span></div>
<div class="abs nav-marker"></div>
<nav class="abs nav"><span>HOME</span><span>ABOUT US</span><span>BLOG</span><span>FAQ's</span><span>CONTACT US</span></nav>
<div class="abs quote">
  <div class="l1">Less pain. Everybody wants it</div>
  <div class="l2">But what are you going to do,</div>
  <div class="l3">once you've got it?"</div>
</div>

<!-- services -->
<div class="abs divider" style="left:205px;top:394px;width:367px"><i style="left:160px;width:66px"></i></div>
<h2 class="abs sec-title" style="left:0;top:410px;width:780px">Our <b>Services</b></h2>
<p class="abs sec-desc" style="left:205px;top:430px;width:370px">Lorem ipsum dolor sit amet, consectetur adipisicing elit, sed do eiusmod tempor incididunt ut labore et dolore magna aliqua. Ut enim ad minim veniam, quis nostrud exercitation ullamco laboris nisi ut aliquip ex ea commodo consequat. Duis aute irure dolor in reprehenderit in voluptate velit esse cillum</p>

<div class="abs card" style="left:156px"><div class="thumb" role="img" aria-label="Photograph of a runner's legs on a track"></div><h4>Lorem Ipsum</h4><p>Lorem ipsum dolor sit amet, consectetur adipisicing elit, sed do eiusmod tempor Lorem ipsum dolor sit amet, consectetur adipisicing elit, sed do eiusmod tempor Lorem ipsum dolor sit amet, consectetur</p><a href="#">Read more</a></div>
<div class="abs card" style="left:326px"><div class="thumb" role="img" aria-label="Photograph of a runner's legs on a track"></div><h4>Lorem Ipsum</h4><p>Lorem ipsum dolor sit amet, consectetur adipisicing elit, sed do eiusmod tempor Lorem ipsum dolor sit amet, consectetur adipisicing elit, sed do eiusmod tempor Lorem ipsum dolor sit amet, consectetur</p><a href="#">Read more</a></div>
<div class="abs card" style="left:496px"><div class="thumb" role="img" aria-label="Photograph of a runner's legs on a track"></div><h4>Lorem Ipsum</h4><p>Lorem ipsum dolor sit amet, consectetur adipisicing elit, sed do eiusmod tempor Lorem ipsum dolor sit amet, consectetur adipisicing elit, sed do eiusmod tempor Lorem ipsum dolor sit amet, consectetur</p><a href="#">Read more</a></div>

<!-- sort me out -->
<div class="abs divider" style="left:162px;top:679px;width:211px"><i style="left:79px;width:57px"></i></div>
<h2 class="abs sec-title" style="left:156px;top:695px;width:222px">Sort me <b>Out</b></h2>
<p class="abs sec-desc" style="left:180px;top:714px;width:175px">Lorem ipsum dolor sit amet, consectetur adipisicing elit, sed do eiusmod tempor incididunt ut labore et dolore magna aliqua. Ut enim</p>
<div class="abs acc-head">LOREM IPSUM DOLOR</div>
<p class="abs acc-body">Lorem ipsum dolor sit amet, consectetur adipisicing elit, sed do eiusmod tempor incididunt ut labore et dolore magna aliqua. Ut enim ad minim veniam, quis nostrud exercitation ullamco laboris nisi ut aliquip ex ea commodo consequat. Duis aute irure dolor in reprehenderit in voluptate velit esse cillum dolore eu fugiat nulla pariatur. Excepteur sint occaecat cupidatat non proident, sunt in culpa qui officia deserunt mollit anim id est laborum.</p>
<div class="abs acc-row" style="top:813px">LOREM IPSUM DOLOR<span>+</span></div>
<div class="abs acc-row" style="top:828px">LOREM IPSUM DOLOR<span>+</span></div>
<div class="abs acc-row" style="top:843px">LOREM IPSUM DOLOR<span>+</span></div>
<div class="abs acc-row" style="top:858px">LOREM IPSUM DOLOR<span>+</span></div>

<!-- blog -->
<div class="abs divider" style="left:399px;top:679px;width:211px"><i style="left:79px;width:57px"></i></div>
<h2 class="abs sec-title" style="left:399px;top:695px;width:211px">Latest from <b>Blog</b></h2>
<p class="abs sec-desc" style="left:418px;top:714px;width:175px">Lorem ipsum dolor sit amet, consectetur adipisicing elit, sed do eiusmod tempor incididunt ut labore et dolore magna aliqua. Ut enim</p>

<div class="abs post" style="top:744px">
  <div class="date"><div class="d1">14<br>DEC</div><div class="d2">13</div></div>
  <h5>LOREM IPSUM</h5>
  <div class="meta"><svg width="8" height="6" viewBox="0 0 8 6"><ellipse cx="4" cy="2.6" rx="3.5" ry="2.2" fill="none" stroke="#aaa" stroke-width=".7"/></svg>5 comments</div>
  <p>Lorem ipsum dolor sit amet, consectetur adipisicing elit, sed do eiusmod tempor incididunt ut labore et dolore magna aliqua. Ut enim ad minim veniam, quis nostrud exercitation ullamco laboris nisi ut aliquip ex ea commodo consequat. <em>read more</em></p>
</div>
<div class="abs post" style="top:816px">
  <div class="date"><div class="d1">14<br>DEC</div><div class="d2">13</div></div>
  <h5>LOREM IPSUM</h5>
  <div class="meta"><svg width="8" height="6" viewBox="0 0 8 6"><ellipse cx="4" cy="2.6" rx="3.5" ry="2.2" fill="none" stroke="#aaa" stroke-width=".7"/></svg>5 comments</div>
  <p>Lorem ipsum dolor sit amet, consectetur adipisicing elit, sed do eiusmod tempor incididunt ut labore et dolore magna aliqua. Ut enim ad minim veniam, quis nostrud exercitation ullamco laboris nisi ut aliquip ex ea commodo consequat. <em>read more</em></p>
</div>

<!-- testimonial -->
<div class="abs divider" style="left:205px;top:915px;width:367px"><i style="left:160px;width:66px"></i></div>
<h2 class="abs sec-title" style="left:0;top:931px;width:780px">What they <b>Say</b></h2>
<p class="abs sec-desc" style="left:325px;top:950px;width:130px">Lorem ipsum dolor sit amet, consectetur adipisicing elit, sed do eiusmod tempor incididunt ut labore et</p>
<p class="abs testimonial">"Lorem ipsum dolor sit amet, consectetur adipisicing elit, sed do eiusmod tempor incididunt ut labore et dolore magna aliqua. Ut enim ad minim veniam, quis nostrud exercitation ullamco"</p>
<p class="abs author"><b>JRL</b>, Graphic Designer</p>

<!-- footer -->
<footer class="abs footer"></footer>
<h3 class="abs f-title" style="left:156px">Quick Links</h3>
<ul class="abs f-links"><li>Home</li><li>About Us</li><li>Blog</li><li>FAQ</li><li>Contact Us</li></ul>

<h3 class="abs f-title" style="left:239px"><b>My</b> work</h3>
<div class="abs f-text" style="left:239px;width:122px">This is Pixelbrook's version of Lorem Ipsum. Proin gravida nibh vel velit auctor aliquet. Aenean sollicitudin, lorem quis bibendum auctor, nisi elit consequat ipsum, nec sagittis sem nibh id elit.<div class="f-more" style="margin-top:4px">Read more <span>&rarr;</span></div></div>

<h3 class="abs f-title" style="left:384px"><b>My</b> Research</h3>
<div class="abs f-text" style="left:384px;width:116px">This is Pixelbrook's version of Lorem Ipsum. Proin gravida nibh vel velit auctor aliquet. Aenean sollicitudin, lorem quis bibendum auctor, nisi elit .<div class="f-more" style="margin-top:4px">Read more <span>&rarr;</span></div></div>

<h3 class="abs f-title" style="left:515px"><b>Our</b> Contact</h3>
<div class="abs contact" style="top:1098px"><svg width="6" height="8" viewBox="0 0 6 8"><path d="M3 0a3 3 0 0 1 3 3c0 2-3 5-3 5S0 5 0 3a3 3 0 0 1 3-3z" fill="#f2be00"/><circle cx="3" cy="3" r="1" fill="#161415"/></svg><span>Lindgate Street 42,<br>Harrowby, Westmark</span></div>
<div class="abs contact" style="top:1121px"><svg width="7" height="7" viewBox="0 0 7 7"><path d="M1.5 0l1.3 1.8-.8 1a4 4 0 0 0 2 2l1-.8L7 5.5 6 7C3 7 0 4 0 1z" fill="#f2be00"/></svg><span>Phone: +123 45 678-910</span></div>
<div class="abs contact" style="top:1144px"><svg width="7" height="5" viewBox="0 0 7 5"><rect width="7" height="5" fill="#f2be00"/><path d="M0 0l3.5 2.6L7 0" fill="none" stroke="#161415" stroke-width=".6"/></svg><span>Email:hello@lindgateclinic.com</span></div>

<div class="abs bottom"><span>Copyright . All Rights Reserved</span></div>

</body>
</html>
```